Halvering & Partners, LLC Business Card 2016

We need a new business card design for a very important trade show coming up.

We are a compliance Consulting Firm. Our clients are stock brokerage firms and investment advisers.

I would like our logo on both sides of the card.

Info in the front of the card shold include:

Logo
First & Last Name
Title
Office #
Cell #
Email
Company Address (42 W. Calloway Blvd., Suite 300 Pasadena, CA 91847

Back of the card should include the logo and url: www.halveringpartnersgroup.com

Target Market(s)

Stock Brokerage Firms and Investment Advisers

Industry/Entity Type

Financial Service

Contact Information for Business Card

Russell K. Halvering
President
42 W. Calloway Blvd., Suite 300
Pasadena, CA 91847
O 626.555.0147 ext. 204
C 818.555.0192
Email: russ@halveringpartnersgroup.com
www.halveringpartnersgroup.com

Requirements
Nice to have
• The back of the card could be black with the logo with the white letters.
• I do want the front of the card to at least have the color logo with the black "Halvering & Partners Lettering.

```html
<!DOCTYPE html>
<html lang="en">
<head>
<meta charset="utf-8">
<title>Halvering &amp; Partners — Business Card</title>
<link rel="stylesheet" href="https://fonts.googleapis.com/css2?family=Cinzel:wght@600&family=Crimson+Text:wght@400&family=Open+Sans:wght@400;700&display=swap">
<style>
  :root {
    --backdrop: #ece9e5;
    --card-white: #ffffff;
    --brand-red: #a8191c;
    --ink: #1d1d1d;
    --ink-soft: #333333;
    --rule: #9a9a9a;
    --grey-light: #f4f4f5;
    --grey-dark: #8c8e97;
    --faint-mark: rgba(168, 25, 28, 0.07);
  }
  * { box-sizing: border-box; margin: 0; padding: 0; }
  html, body { width: 1200px; height: 450px; overflow: hidden; }
  body {
    background: var(--backdrop);
    position: relative;
    font-family: "Open Sans", Arial, sans-serif;
  }
  .card {
    position: absolute;
    top: 80px;
    width: 540px;
    height: 290px;
    box-shadow: 0 6px 18px rgba(0,0,0,0.22);
    overflow: hidden;
  }
  .card--front { left: 30px; background: var(--card-white); }
  .card--back {
    left: 630px;
    background: radial-gradient(ellipse at 45% 45%, var(--grey-light) 0%, #d6d7db 45%, var(--grey-dark) 100%);
  }

  /* Brand lockup */
  .brand { position: absolute; display: flex; align-items: center; gap: 14px; }
  .brand__square { background: var(--brand-red); flex: none; }
  .brand__name {
    font-family: "Cinzel", "Times New Roman", serif;
    font-weight: 600;
    color: var(--ink);
    line-height: 1;
    letter-spacing: 0.02em;
    white-space: nowrap;
  }
  .card--front .brand { left: 24px; top: 36px; }
  .card--front .brand__square { width: 52px; height: 52px; }
  .card--front .brand__name { font-size: 30px; }

  .faint-mark {
    position: absolute;
    right: 24px;
    top: 170px;
    width: 96px;
    height: 96px;
    background: var(--faint-mark);
  }

  .holder {
    position: absolute;
    right: 22px;
    top: 122px;
    font-size: 16px;
    color: var(--ink-soft);
    white-space: nowrap;
  }
  .holder__name { color: var(--brand-red); font-weight: 700; }
  .divider {
    position: absolute;
    left: 40px;
    right: 0;
    top: 152px;
    height: 2px;
    background: linear-gradient(to right, rgba(154,154,154,0), var(--rule) 60%, #777);
  }

  .contacts {
    position: absolute;
    left: 26px;
    top: 176px;
    list-style: none;
    font-size: 13px;
    color: var(--ink);
  }
  .contacts li { display: flex; align-items: center; gap: 10px; height: 20px; white-space: nowrap; }
  .contacts svg { width: 13px; height: 13px; fill: var(--brand-red); flex: none; }
  .contacts .icon-globe { fill: none; stroke: var(--brand-red); stroke-width: 1.6; }

  /* Back side */
  .card--back .brand {
    left: 0; right: 0; top: 92px;
    flex-direction: column;
    gap: 14px;
  }
  .card--back .brand__square { width: 70px; height: 70px; }
  .card--back .brand__name { font-size: 26px; }
  .web-address {
    position: absolute;
    left: 0; right: 0; top: 222px;
    text-align: center;
    font-family: "Crimson Text", Georgia, serif;
    font-size: 19px;
    color: var(--ink);
  }
  .web-address__domain { color: var(--brand-red); }
</style>
</head>
<body>

<section class="card card--front" aria-label="Card front">
  <div class="brand">
    <span class="brand__square"></span>
    <span class="brand__name">Halvering &amp; Partners</span>
  </div>
  <div class="faint-mark"></div>
  <p class="holder"><span class="holder__name">Russell K. Halvering,</span> President</p>
  <div class="divider"></div>
  <ul class="contacts">
    <li>
      <svg viewBox="0 0 16 16" aria-hidden="true"><path d="M4 1l3 3-2 2c1 2 3 4 5 5l2-2 3 3-2 3C7 15 1 9 1 3z"/></svg>
      O 626.555.0147 ext. 204
    </li>
    <li>
      <svg viewBox="0 0 16 16" aria-hidden="true"><path d="M4 0h8v16H4zM5.5 2v10h5V2zM7 13h2v1.5H7z"/></svg>
      C 818.555.0192
    </li>
    <li>
      <svg viewBox="0 0 16 16" aria-hidden="true"><path d="M1 3h14v10H1zM2.5 4.5v.6L8 9l5.5-3.9v-.6z"/></svg>
      russ@halveringpartnersgroup.com
    </li>
    <li>
      <svg class="icon-globe" viewBox="0 0 16 16" aria-hidden="true"><circle cx="8" cy="8" r="6.5"/><ellipse cx="8" cy="8" rx="2.8" ry="6.5"/><path d="M1.5 8h13"/></svg>
      www.halveringpartnersgroup.com
    </li>
    <li>
      <svg viewBox="0 0 16 16" aria-hidden="true"><path d="M8 0a5.5 5.5 0 0 0-5.5 5.5C2.5 10 8 16 8 16s5.5-6 5.5-10.5A5.5 5.5 0 0 0 8 0zm0 3a2.5 2.5 0 1 1 0 5 2.5 2.5 0 0 1 0-5z"/></svg>
      42 W. Calloway Blvd., Suite 300 Pasadena, CA 91847
    </li>
  </ul>
</section>

<section class="card card--back" aria-label="Card back">
  <div class="brand">
    <span class="brand__square"></span>
    <span class="brand__name">Halvering &amp; Partners</span>
  </div>
  <p class="web-address">www.<span class="web-address__domain">halveringpartnersgroup</span>.com</p>
</section>

</body>
</html>
```